Calder Pizza - Takeout Menu Design

We are looking for a takeout menu design.
We are looking for a( 5" x 8.5" DOUBLE SIDED) flyer with our available pizza flavors
Must be easy to ready and not "busy"

Must include our logo (attached)
website: www.calderpizza.ca
address:
Fenwick Ridge Plaza
417, 318 9 Avenue SW
and the following details:
Visit our website for our complete appetizer, pasta, salad and catering menu.

Winner of this contest will also be offered to create a few print designs via printhive.

Please do not hesitate to ask any questions.

Target Market(s)

Business / Office clientele

Industry/Entity Type

Pizza place / specializing in corporate orders

Requirements
Must have
• Easy to read
Should not have
• Can not be busy or cluttered

```html
<!DOCTYPE html>
<html lang="en">
<head>
<meta charset="utf-8">
<title>Calder Pizza – Takeout Menu</title>
<link href="https://fonts.googleapis.com/css2?family=Alegreya:ital,wght@0,700;1,400&family=Heebo:wght@300&family=Krona+One&family=Playfair+Display:wght@900&family=Lato:wght@300;400&display=swap" rel="stylesheet">
<style>
  :root {
    --backdrop: #262626;
    --paper: #ffffff;
    --ink: #1c1c1c;
    --ink-soft: #3a3a3a;
    --red: #c1272d;
    --rule: #c9c9c9;
  }
  * { margin: 0; padding: 0; box-sizing: border-box; }
  html, body { width: 1200px; height: 1037px; overflow: hidden; background: var(--backdrop); }
  .canvas { position: relative; width: 1200px; height: 1037px; }
  .page {
    position: absolute; top: 92px; width: 502px; height: 853px;
    background: var(--paper); color: var(--ink);
  }
  .page--front { left: 83px; }
  .page--back { left: 615px; }

  .brand {
    position: absolute; left: 0; right: 0; text-align: center;
    font-family: "Lato", sans-serif; font-weight: 300; color: var(--ink);
    letter-spacing: 0.5px; text-transform: uppercase;
  }
  .page--front .brand { top: 27px; font-size: 17px; }
  .page--back .brand { top: 18px; font-size: 28px; }

  .title-frame {
    position: absolute; left: 130px; top: 38px; width: 242px; height: 59px;
    border: 1.5px solid var(--ink); border-top: none;
  }
  .title-frame::before, .title-frame::after {
    content: ""; position: absolute; top: 0; height: 1.5px; width: 16px; background: var(--ink);
  }
  .title-frame::before { left: 0; }
  .title-frame::after { right: 0; }
  .title-word {
    position: absolute; left: 0; right: 0; top: 46px; text-align: center;
    font-family: "Playfair Display", serif; font-weight: 900; font-size: 40px;
    letter-spacing: 3px; line-height: 1;
  }
  .title-script {
    position: absolute; left: 166px; top: 84px; width: 156px; height: 50px;
    background: linear-gradient(100deg, rgba(193,39,45,0.85), rgba(193,39,45,0.6));
    border-radius: 24px 8px 24px 8px;
  }

  .intro {
    position: absolute; left: 40px; right: 40px; top: 145px; text-align: center;
    font-family: "Heebo", sans-serif; font-weight: 300; font-size: 11px; line-height: 17px;
    color: var(--ink-soft);
  }

  .ribbon {
    position: absolute; left: 124px; width: 255px; height: 24px;
    display: flex; align-items: center; justify-content: center;
    font-family: "Alegreya", serif; font-weight: 700; font-size: 10px;
    letter-spacing: 0.8px; color: #fff; text-transform: uppercase;
  }
  .ribbon svg { position: absolute; inset: 0; width: 100%; height: 100%; z-index: 0; }
  .ribbon span { position: relative; z-index: 1; }
  .ribbon--classic { top: 197px; }
  .ribbon--specialty { top: 468px; }

  .menu-list { position: absolute; left: 35px; width: 432px; list-style: none; }
  .classic-list { top: 230px; }
  .specialty-list { top: 510px; }
  .page--back .menu-list { left: 35px; top: 97px; width: 434px; }

  .item {
    position: relative; display: flex; justify-content: space-between; align-items: flex-start;
    border-bottom: 1px dashed var(--rule);
  }
  .classic-list .item { height: 28px; align-items: center; }
  .specialty-list .item { height: 39px; padding-top: 5px; }
  .page--back .item { height: 40.9px; padding-top: 5px; }

  .item-name-plain {
    font-family: "Krona One", sans-serif; font-size: 9.5px; letter-spacing: 0.3px;
    text-transform: uppercase; color: var(--ink);
  }
  .item-name {
    font-family: "Alegreya", serif; font-weight: 700; font-size: 12.5px;
    letter-spacing: 0.8px; text-transform: uppercase; line-height: 14px;
  }
  .item-desc {
    font-family: "Alegreya", serif; font-style: italic; font-size: 9px;
    color: var(--ink-soft); line-height: 11px; letter-spacing: 0.2px;
  }
  .prices {
    display: flex; gap: 0; font-family: "Krona One", sans-serif; font-size: 9.5px;
    color: var(--red); line-height: 14px;
  }
  .prices span { display: inline-block; width: 57px; }
  .prices span:last-child { width: 49px; text-align: right; }
  .price-stack { display: flex; flex-direction: column; gap: 1px; }

  .banner-line {
    position: absolute; top: 80px; left: 32px; width: 437px; height: 1px; background: var(--red);
  }
  .banner {
    position: absolute; left: 170px; top: 70px; width: 162px; height: 22px;
    background: var(--red); border-radius: 6px; color: #fff;
    font-family: "Alegreya", serif; font-weight: 700; font-size: 15px; letter-spacing: 1.2px;
    display: flex; align-items: center; justify-content: center;
  }
</style>
</head>
<body>
<div class="canvas">

  <section class="page page--front">
    <div class="brand">Calder Pizza</div>
    <div class="title-frame"></div>
    <div class="title-word">TAKEOUT</div>
    <div class="title-script" role="img" aria-label="Hand-lettered red script word “Menu”"></div>
    <p class="intro">All Of Our Pizzas Are Prepared Fresh Everyday Using Only The Finest Mozzarella Blend And Ingredients.</p>

    <div class="ribbon ribbon--classic">
      <svg viewBox="0 0 255 24" preserveAspectRatio="none"><polygon points="0,0 255,0 245,12 255,24 0,24 10,12" fill="#c1272d"/></svg>
      <span>Classic Take-Out Pizza – 8" &amp; 13"</span>
    </div>
    <ul class="menu-list classic-list">
      <li class="item"><span class="item-name-plain">Pepperoni &amp; Mushroom</span><span class="prices"><span>$12.99</span><span>$30.95</span></span></li>
      <li class="item"><span class="item-name-plain">Pepperoni</span><span class="prices"><span>$11.99</span><span>$29.95</span></span></li>
      <li class="item"><span class="item-name-plain">Hawaiian</span><span class="prices"><span>$12.99</span><span>$30.95</span></span></li>
      <li class="item"><span class="item-name-plain">Pepperoni &amp; Ham</span><span class="prices"><span>$12.99</span><span>$30.95</span></span></li>
      <li class="item"><span class="item-name-plain">Pepperoni &amp; Ham</span><span class="prices"><span>$12.99</span><span>$30.95</span></span></li>
      <li class="item"><span class="item-name-plain">Ham &amp; Mushroom</span><span class="prices"><span>$12.99</span><span>$30.95</span></span></li>
      <li class="item"><span class="item-name-plain">Beef &amp; Onion</span><span class="prices"><span>$13.49</span><span>$32.95</span></span></li>
      <li class="item"><span class="item-name-plain">Cheese</span><span class="prices"><span>$11.99</span><span>$29.95</span></span></li>
    </ul>

    <div class="ribbon ribbon--specialty">
      <svg viewBox="0 0 255 24" preserveAspectRatio="none"><polygon points="0,0 255,0 245,12 255,24 0,24 10,12" fill="#c1272d"/></svg>
      <span>Specialty Take-Out Pizza- 8" &amp; 13"</span>
    </div>
    <ul class="menu-list specialty-list">
      <li class="item"><div><div class="item-name">Pepperoni &amp; Mushroom</div><div class="item-desc">Pepperoni, Beef &amp; Smoked Ham &amp; Bacon</div></div><span class="prices"><span>$14.99</span><span>$35.95</span></span></li>
      <li class="item"><div><div class="item-name">Double Pepperoni</div><div class="item-desc">Loads of Pepperoni</div></div><span class="prices"><span>$13.49</span><span>$32.95</span></span></li>
      <li class="item"><div><div class="item-name">Hot Honey Pepperoni</div><div class="item-desc">Double Pepperoni and drizzled with Hot Honey</div></div><span class="prices"><span>$14.49</span><span>$34.95</span></span></li>
      <li class="item"><div><div class="item-name">Hawaiian Heat</div><div class="item-desc">Smoked Ham, Pineapple and Banana Peppers</div></div><span class="prices"><span>$13.49</span><span>$32.95</span></span></li>
      <li class="item"><div><div class="item-name">Four Cheese</div><div class="item-desc">Mozzarella, Feta, Romano and Cheddar Cheese</div></div><span class="prices"><span>$13.49</span><span>$32.95</span></span></li>
      <li class="item"><div><div class="item-name">Montreal</div><div class="item-desc">Pepperoni &amp; Double Smoked Bacon</div></div><span class="prices"><span>$13.49</span><span>$32.95</span></span></li>
      <li class="item"><div><div class="item-name">Montreal Heat</div><div class="item-desc">Pepperoni, Double Smoked Bacon &amp; Banana Peppers</div></div><span class="prices"><span>$13.99</span><span>$33.95</span></span></li>
      <li class="item"><div><div class="item-name">Supreme</div><div class="item-desc">Pepperoni, Mushrooms &amp; Green Peppers</div></div><span class="prices"><span>$13.49</span><span>$32.95</span></span></li>
    </ul>
  </section>

  <section class="page page--back">
    <div class="brand">Calder Pizza</div>
    <div class="banner-line"></div>
    <div class="banner">TAKEOUT MENU</div>
    <ul class="menu-list">
      <li class="item"><div><div class="item-name">Canadian</div><div class="item-desc">Pepperoni, Mushrooms &amp; Ham</div></div><span class="prices"><span>$13.49</span><span>$32.95</span></span></li>
      <li class="item"><div><div class="item-name">BBQ Chicken</div><div class="item-desc">Chicken Breast, Hickory BBQ Sauce, Red Onions &amp; Banana Peppers</div></div><span class="prices"><span>$13.99</span><span>$33.95</span></span></li>
      <li class="item"><div><div class="item-name">BBQ Chicken Plus</div><div class="item-desc">Chicken Breast, Hickory BBQ Sauce, Red Onions &amp; Cilantro</div></div><span class="prices"><span>$14.79</span><span>$34.95</span></span></li>
      <li class="item"><div><div class="item-name">Spicy BBQ Chicken</div><div class="item-desc">Chicken Breast, Hickory BBQ Sauce, Red Onions &amp; Banana Peppers</div></div><span class="prices"><span>$14.49</span><span>$35.95</span></span></li>
      <li class="item"><div><div class="item-name">Sweet Chili Chicken</div><div class="item-desc">Chicken Breast, Pineapple, Red Onions &amp; Sweet Chili Sauce</div></div><span class="prices"><span>$14.49</span><span>$35.95</span></span></li>
      <li class="item"><div><div class="item-name">Chicken Club</div><div class="item-desc">Chicken Breast, Double Smoked Bacon, Red Onions and Tomatoes</div></div><span class="prices"><span>$14.79</span><span>$35.95</span></span></li>
      <li class="item"><div><div class="item-name">Athenean</div><div class="item-desc">Chicken Breast, Spinach, Feta Cheese and Tomato</div></div><span class="prices"><span>$14.49</span><span>$34.95</span></span></li>
      <li class="item"><div><div class="item-name">Greek Supreme</div><div class="item-desc">Chicken Breast, Feta Cheese, Tomato, Green Pepper, Red Onions &amp; Black Olives</div></div><span class="prices"><span>$14.99</span><span>$35.95</span></span></li>
      <li class="item"><div><div class="item-name">Mediterranean Chicken</div><div class="item-desc">Seasoned Chicken Breast, Tomatoes, Red Onions and Feta Cheese</div></div><span class="prices"><span>$14.79</span><span>$35.95</span></span></li>
      <li class="item"><div><div class="item-name">Original Spinach</div><div class="item-desc">Spinach &amp; Feta Cheese</div></div><span class="prices"><span>$13.49</span><span>$32.95</span></span></li>
      <li class="item"><div><div class="item-name">Zeus</div><div class="item-desc">Spinach, Feta Cheese and Tomatoes</div></div><span class="prices"><span>$13.95</span><span>$33.95</span></span></li>
      <li class="item"><div><div class="item-name">Greek</div><div class="item-desc">Feta Cheese, Tomato, Green Peppers, Red Onions and Black Olives</div></div><span class="prices"><span>$13.99</span><span>$33.95</span></span></li>
      <li class="item"><div><div class="item-name">Vegetarian</div><div class="item-desc">Mushrooms, Tomatoes, Green Peppers and Black Olives</div></div><span class="prices"><span>$13.49</span><span>$32.95</span></span></li>
      <li class="item"><div><div class="item-name">Veggie Delight</div><div class="item-desc">Mushrooms, Tomatoes, Green Peppers, Black Olives &amp; Onions</div></div><span class="prices"><span>$13.95</span><span>$33.95</span></span></li>
      <li class="item"><div><div class="item-name">Deluxe</div><div class="item-desc">Pepperoni, Mushrooms, Ham, Tomatoes, Green Peppers and Red Onions</div></div><span class="prices"><span>$14.49</span><span>$34.95</span></span></li>
      <li class="item"><div><div class="item-name">Calder Special</div><div class="item-desc">Pepperoni, Mushrooms, Ham, Green Peppers and Black Olives</div></div><span class="prices"><span>$14.49</span><span>$34.95</span></span></li>
      <li class="item"><div><div class="item-name">Dill Pickle</div><div class="item-desc">Crispy Dill Pickles, Fresh Dill with our cream based garlic sauce.<br>Served with our without bacon.</div></div><span class="price-stack"><span class="prices"><span>$13.49</span><span>$32.95</span></span><span class="prices"><span>$14.49</span><span>$35.95</span></span></span></li>
      <li class="item" style="border-bottom:none"><div><div class="item-name">BBQ Pulled Pork</div><div class="item-desc">Pulled Pork, Red Onions, Red Peppers and Cilantro.</div></div><span class="prices"><span>$14.49</span><span>$35.95</span></span></li>
    </ul>
  </section>

</div>
</body>
</html>
```